Popup Nightclub Grand Opening Flyer

We need to design a flyer for the grand opening of an upscale, exclusive nightclub called "Lanternfall". The design needs to be chic and exclusive. The background should be black and the text should primarily be white. We like minimalist designs.

Here is the text for the flyer
-
Velvetrope Atlanta Presents

Lanternfall (LOGO)

A Popup Nightclub Experience
For one night Only

Friday, October 18, 2013
Party begins at 9PM

INVITE ONLY

See invitation for location details
(Velvetrope Atlanta logo)

-
Examples we like

http://cdn2-b.brivelpost.com/sites/default/files/styles/image_content_width/hash/3d/fa/1472093815_4471_flyer.jpg?itok=R8kqWm2z

http://api.plovra.com/files/7Kqq-Tr82XXB3pQzJvmtR5HL2W719E4nbRtC6KLd4HsfM8Y2qTDK-VmjwDoNqLX4QBzTHD9nakRbVx3m-Pfq8htc3MDTWr5p4/2zelSaturdays.jpg

http://quenmar.com/wp-content/uploads/yootheme/widgetkit/gallery/2zel/2zel-gen_vroom4-01.jpg

Hi All, one thing that we are seeing that we don't like is on over emphasis on the phrase "a popup nightclub experience" please don't make this the largest thing on the flyer

Target Market(s)

Target market is 25-35 year olds who are affluent (rich) and like luxury brands

Requirements
Must have
• Dark Background
Nice to have
• Velvetrope Logo on the bottom
Modern text that isn't curvy
Should not have
• Curved text

```html
<!DOCTYPE html>
<html lang="en">
<head>
<meta charset="utf-8">
<title>Lanternfall — A Popup Nightclub Experience</title>
<link rel="stylesheet" href="https://fonts.googleapis.com/css2?family=Poppins:wght@300;600;700&display=swap">
<style>
  :root {
    --ink-black: #050505;
    --bg-glow: #1c1c1c;
    --text-white: #ffffff;
    --text-silver: #9a9a9a;
    --text-grey: #8a8a8a;
    --accent-yellow: #fff01f;
    --mark-grey: #b9b9b9;
    --rule-white: #d8d8d8;
  }
  html, body {
    margin: 0;
    padding: 0;
    width: 827px;
    height: 1200px;
    overflow: hidden;
    background: var(--ink-black);
  }
  .flyer {
    position: relative;
    width: 827px;
    height: 1200px;
    overflow: hidden;
    font-family: "Poppins", sans-serif;
    color: var(--text-white);
    text-align: center;
  }
  .flyer-backdrop {
    position: absolute;
    inset: 0;
    background: radial-gradient(ellipse 70% 55% at 50% 38%, var(--bg-glow) 0%, #0e0e0e 55%, var(--ink-black) 100%);
  }
  .line {
    position: absolute;
    left: 0;
    width: 100%;
    margin: 0;
    line-height: 1;
    white-space: nowrap;
  }
  .presenter {
    top: 22px;
    font-weight: 700;
    font-size: 31px;
    color: var(--text-silver);
    line-height: 1.05;
    letter-spacing: -0.3px;
  }
  .club-mark {
    position: absolute;
    left: 243px;
    top: 262px;
  }
  .club-name {
    top: 660px;
    font-weight: 300;
    font-size: 52px;
    letter-spacing: 9px;
    color: #e4e4e4;
    text-transform: uppercase;
  }
  .tagline {
    top: 758px;
    font-weight: 600;
    font-size: 34px;
    letter-spacing: -0.3px;
  }
  .tagline-text {
    display: inline-block;
    padding-bottom: 12px;
    border-bottom: 1px solid var(--rule-white);
  }
  .one-night {
    top: 826px;
    font-weight: 700;
    font-size: 50px;
    letter-spacing: -0.5px;
    color: var(--accent-yellow);
    text-shadow: 0 0 14px rgba(255, 240, 31, 0.55);
  }
  .event-date {
    top: 904px;
    font-weight: 700;
    font-size: 28px;
    letter-spacing: 1.5px;
    color: var(--text-grey);
  }
  .invite-only {
    top: 1006px;
    font-weight: 600;
    font-size: 28px;
  }
  .location-note {
    top: 1054px;
    font-weight: 600;
    font-size: 13px;
    letter-spacing: 0.2px;
  }
  .host-name {
    top: 1128px;
    font-weight: 300;
    font-size: 28px;
    letter-spacing: 3px;
    color: #e6e6e6;
  }
</style>
</head>
<body>
  <main class="flyer">
    <div class="flyer-backdrop" role="img" aria-label="Black damask-style floral pattern background"></div>

    <p class="line presenter">VELVETROPE ATLANTA<br>PRESENTS</p>

    <svg class="club-mark" width="340" height="340" viewBox="0 0 340 340" aria-hidden="true">
      <circle cx="170" cy="170" r="169" fill="var(--mark-grey)"/>
    </svg>
    <p class="line club-name">Lanternfall</p>

    <p class="line tagline"><span class="tagline-text">A POPUP NIGHTCLUB EXPERIENCE</span></p>
    <p class="line one-night">FOR ONE NIGHT ONLY</p>
    <p class="line event-date">FRIDAY OCTOBER 18 2013 @ 9:00PM</p>

    <p class="line invite-only">INVITE ONLY</p>
    <p class="line location-note">SEE INVITATION FOR LOCATION DETAILS</p>

    <p class="line host-name">VELVETROPE ATLANTA</p>
  </main>
</body>
</html>
```